Magazine Ad for the Waste Industry

We need a full page ad design that will help us introduce our new engine cooling system into the Waste market. This system helps regulate engine temperatures for large trash trucks with its advanced technology and durable. We would like this ad to make an impact and stand out from the more cluttered looking ads that are seen in trade magazines.
The project must be submitted in either InDesign or Photoshop files.

Target Market(s)

Waste Industry, Trash truck manufacturers

Industry/Entity Type

Waste Management

Font styles to use
Sans Serif

Colors
0255a3

Requirements
Must have
• The text and images attached with a more modern industrial/masculine feel.
• Our Company colors are...
• Blue (RGB 25, 76, 159)
• Gray (RGB 129, 130, 133)
• White and black as accents as needed
• SIZING
• Spread Bleed: 9.5" x 11.375"
Nice to have
• I attached two files for a font that we have used in the past. Another font we use commonly is Ariel.

```html
<!DOCTYPE html>
<html lang="en">
<head>
<meta charset="utf-8">
<title>Advanced Electric Engine Cooling</title>
<link href="https://fonts.googleapis.com/css2?family=Michroma&family=Archivo:wght@700;800&display=swap" rel="stylesheet">
<style>
  :root {
    --deep-navy: #04122a;
    --brand-blue: #0255a3;
    --ice-blue: #4f9fd8;
    --steel: #818285;
    --silver-light: #f2f3f5;
    --gold: #f1c94e;
    --gold-deep: #c99a2a;
    --white: #ffffff;
    --black: #000000;
  }
  * { margin: 0; padding: 0; box-sizing: border-box; }
  html, body { width: 845px; height: 1200px; overflow: hidden; background: var(--black); }
  .ad {
    position: relative;
    width: 845px;
    height: 1200px;
    overflow: hidden;
    background:
      radial-gradient(ellipse 420px 340px at 50% 42%, rgba(170,215,245,0.75), rgba(60,140,205,0.35) 55%, transparent 80%),
      linear-gradient(180deg, #0a2a55 0%, #1a5a95 30%, #10447c 55%, #06214a 75%, var(--deep-navy) 100%);
  }
  .headline {
    position: absolute;
    left: 0; right: 0; top: 70px;
    text-align: center;
    font-family: "Michroma", sans-serif;
    line-height: 1;
  }
  .headline .line { display: block; white-space: nowrap; }
  .headline .silver {
    background: linear-gradient(180deg, var(--silver-light) 0%, #b9bcc2 45%, #8a8d93 60%, #d9dbde 100%);
    -webkit-background-clip: text;
    background-clip: text;
    color: transparent;
  }
  .headline .advanced { font-size: 71px; letter-spacing: -2px; transform: scaleY(1.25); margin-left: 20px; }
  .headline .electric { font-size: 86px; letter-spacing: -3px; transform: scaleY(1.2); margin-top: 24px; margin-left: 14px; }
  .headline .cooling {
    font-size: 50px; letter-spacing: -2px; margin-top: 22px; margin-left: 16px;
    color: var(--gold);
    transform: scaleY(1.05);
  }
  .product-photo {
    position: absolute;
    left: 232px; top: 336px;
    width: 498px; height: 520px;
    background: radial-gradient(ellipse at 50% 45%, #6d7680 0%, #2b3036 55%, #14171b 100%);
    clip-path: polygon(6% 20%, 40% 0%, 78% 12%, 100% 48%, 92% 92%, 42% 100%, 4% 66%);
  }
  .swoosh { position: absolute; left: 0; top: 840px; width: 845px; height: 160px; }
  .bottom-band { position: absolute; left: 0; top: 930px; width: 845px; height: 270px; background: var(--black); }
  .benefit {
    position: absolute;
    display: flex;
    align-items: center;
    gap: 10px;
    font-family: "Archivo", sans-serif;
    font-weight: 800;
    font-style: italic;
    font-size: 17px;
    line-height: 18px;
    letter-spacing: 0.3px;
  }
  .benefit.gold { color: var(--gold); }
  .benefit.white { color: var(--white); }
  .benefit svg { flex: none; width: 16px; height: 30px; }
  .b-horsepower { left: 603px; top: 940px; }
  .b-reversible { left: 370px; top: 1002px; }
  .b-fuel { left: 603px; top: 1002px; }
  .b-maintenance { left: 370px; top: 1082px; }
  .b-quiet { left: 603px; top: 1082px; }
  .brand {
    position: absolute; left: 64px; top: 1058px;
    display: flex; align-items: center; gap: 14px;
  }
  .brand-name {
    font-family: "Archivo", sans-serif; font-weight: 800;
    font-size: 34px; letter-spacing: -0.5px; color: var(--white);
  }
  .partner-badge { width: 68px; height: 54px; background: var(--white); }
  .web {
    position: absolute; left: 66px; top: 1122px;
    font-family: "Archivo", sans-serif; font-weight: 700;
    font-size: 13px; letter-spacing: 0.6px; color: var(--white);
  }
</style>
</head>
<body>
<main class="ad">
  <h1 class="headline">
    <span class="line silver advanced">ADVANCED</span>
    <span class="line silver electric">ELECTRIC</span>
    <span class="line cooling">ENGINE COOLING</span>
  </h1>

  <div class="product-photo" role="img" aria-label="Electric cooling module with four fans bursting through icy spray"></div>

  <svg class="swoosh" viewBox="0 0 845 160" preserveAspectRatio="none" aria-hidden="true">
    <defs>
      <linearGradient id="goldSweep" x1="0" x2="1" y1="0" y2="0">
        <stop offset="0" stop-color="#f6dc8a"/>
        <stop offset="0.45" stop-color="#e8c057"/>
        <stop offset="1" stop-color="#c99a2a" stop-opacity="0"/>
      </linearGradient>
    </defs>
    <path d="M0 70 C 180 130, 380 100, 560 20 C 420 95, 220 120, 0 95 Z" fill="url(#goldSweep)"/>
    <path d="M0 95 C 220 125, 420 100, 600 40 C 600 80, 845 80, 845 90 L 845 160 L 0 160 Z" fill="#000"/>
  </svg>
  <div class="bottom-band"></div>

  <div class="benefit gold b-horsepower">
    <svg viewBox="0 0 16 30"><path d="M2 3 L8 15 L2 27 M8 3 L14 15 L8 27" fill="none" stroke="#f1c94e" stroke-width="1.6"/></svg>
    <span>INCREASE<br>HORSEPOWER</span>
  </div>
  <div class="benefit gold b-reversible">
    <svg viewBox="0 0 16 30"><path d="M2 3 L8 15 L2 27 M8 3 L14 15 L8 27" fill="none" stroke="#f1c94e" stroke-width="1.6"/></svg>
    <span>FULLY<br>REVERSIBLE<br>FANS</span>
  </div>
  <div class="benefit white b-fuel">
    <svg viewBox="0 0 16 30"><path d="M2 3 L8 15 L2 27 M8 3 L14 15 L8 27" fill="none" stroke="#ffffff" stroke-width="1.6"/></svg>
    <span>AVERAGE<br>8% FUEL<br>ECONOMY</span>
  </div>
  <div class="benefit white b-maintenance">
    <svg viewBox="0 0 16 30"><path d="M2 3 L8 15 L2 27 M8 3 L14 15 L8 27" fill="none" stroke="#ffffff" stroke-width="1.6"/></svg>
    <span>ELIMINATE<br>PREVENTATIVE<br>MAINTENANCE</span>
  </div>
  <div class="benefit gold b-quiet">
    <svg viewBox="0 0 16 30"><path d="M2 3 L8 15 L2 27 M8 3 L14 15 L8 27" fill="none" stroke="#f1c94e" stroke-width="1.6"/></svg>
    <span>QUIETER<br>RESIDENTIAL<br>OPERATION</span>
  </div>

  <div class="brand">
    <span class="brand-name">NORVANE</span>
    <span class="partner-badge"></span>
  </div>
  <div class="web">www.norvane-thermal.com/refuse</div>
</main>
</body>
</html>
```